Local Roofing Company Billboard Design

We need a billboard design for an 8' x 32' billboard. This billboard would need to be easily readable and stand out well.
I have uploaded a design that we like - simple, readable, and gets the point across. We do NOT want the $1000 off offer included.
We are looking for a black background with white copy so it will stand out. We want the following on the billboard:
Corvella Roofing logo
corvella-roofing-example.com (optional)
555.214.7736 (mandatory)
Photo is optional, depends on how it all lays out
Production file must comply with layout requirements (uploaded).
Target Market(s)
Homeowners
Font styles to use
Other font styles liked:
- match font from logo
Colors
Designer to choose colors to be used in the design.
Requirements
Must have
- Black background, white copy, logo must be large and legible. Colors used must match our logo colors.

```html
<!DOCTYPE html>
<html lang="en">
<head>
<meta charset="utf-8">
<title>Corvella Roofing Billboard</title>
<link href="https://fonts.googleapis.com/css2?family=Arvo:wght@700&family=Bree+Serif&family=Roboto+Condensed:wght@700&display=swap" rel="stylesheet">
<style>
  :root {
    --page: #e9ecef;
    --board: #000000;
    --orange: #e8581a;
    --white: #ffffff;
    --photo-light: #a9a9a9;
    --photo-dark: #3c3c3c;
  }
  * { box-sizing: border-box; margin: 0; padding: 0; }
  html, body { width: 1200px; height: 1200px; overflow: hidden; background: var(--page); }
  .billboard {
    position: absolute; left: 30px; top: 430px;
    width: 1140px; height: 340px;
    background: var(--board); overflow: hidden;
  }
  .billboard-shapes { position: absolute; inset: 0; }
  .brand-name {
    position: absolute; left: 500px; width: 560px; top: 66px;
    text-align: center;
    font-family: "Arvo", serif; font-weight: 700; font-size: 48px;
    color: var(--white); line-height: 1;
  }
  .services {
    position: absolute; left: 450px; width: 680px; top: 150px;
    list-style: none; display: flex; flex-wrap: wrap; justify-content: center;
    column-gap: 18px; row-gap: 12px;
    font-family: "Bree Serif", serif; font-size: 24px; color: var(--white); line-height: 1.1;
  }
  .services li { display: flex; align-items: center; gap: 6px; white-space: nowrap; }
  .services .break { flex-basis: 100%; height: 0; }
  .tick { width: 19px; height: 19px; flex: none; }
  .phone {
    position: absolute; left: 14px; top: 268px; height: 60px;
    display: flex; align-items: center; gap: 8px;
    font-family: "Roboto Condensed", sans-serif; font-weight: 700; font-size: 46px;
    color: var(--white); line-height: 1;
  }
  .phone-icon { width: 24px; height: 30px; flex: none; }
  .website {
    position: absolute; left: 420px; width: 710px; top: 268px; height: 60px;
    display: flex; align-items: center; gap: 10px;
    font-family: "Arvo", serif; font-weight: 700; font-size: 34px;
    color: var(--board); line-height: 1; white-space: nowrap;
  }
  .globe-icon { width: 38px; height: 38px; flex: none; }
</style>
</head>
<body>
  <section class="billboard">
    <svg class="billboard-shapes" width="1140" height="340" viewBox="0 0 1140 340">
      <defs>
        <linearGradient id="photoTone" x1="0" y1="0" x2="1" y2="1">
          <stop offset="0" stop-color="var(--photo-light)"/>
          <stop offset="1" stop-color="var(--photo-dark)"/>
        </linearGradient>
      </defs>
      <polygon class="house-photo" role="img" aria-label="Black and white photo of a house with a shingle roof under a cloudy sky"
               points="0,0 480,0 400,255 0,255" fill="url(#photoTone)"/>
      <polygon class="accent-stripe" points="500,0 524,0 440,190 416,190" fill="var(--orange)"/>
      <polygon class="web-band" points="398,255 1140,255 1140,340 370,340" fill="var(--orange)"/>
    </svg>

    <h1 class="brand-name">Corvella Roofing</h1>

    <ul class="services">
      <li><svg class="tick" viewBox="0 0 20 20"><circle cx="10" cy="10" r="8.5" fill="none" stroke="var(--orange)" stroke-width="2"/><path d="M5.5 10.5l3 3 6-7" fill="none" stroke="var(--orange)" stroke-width="2.2"/></svg>Standing Seam Metal Roofing</li>
      <li><svg class="tick" viewBox="0 0 20 20"><circle cx="10" cy="10" r="8.5" fill="none" stroke="var(--orange)" stroke-width="2"/><path d="M5.5 10.5l3 3 6-7" fill="none" stroke="var(--orange)" stroke-width="2.2"/></svg>Asphalt Shingle Roofing</li>
      <li class="break"></li>
      <li><svg class="tick" viewBox="0 0 20 20"><circle cx="10" cy="10" r="8.5" fill="none" stroke="var(--orange)" stroke-width="2"/><path d="M5.5 10.5l3 3 6-7" fill="none" stroke="var(--orange)" stroke-width="2.2"/></svg>Tile Roofing</li>
      <li><svg class="tick" viewBox="0 0 20 20"><circle cx="10" cy="10" r="8.5" fill="none" stroke="var(--orange)" stroke-width="2"/><path d="M5.5 10.5l3 3 6-7" fill="none" stroke="var(--orange)" stroke-width="2.2"/></svg>Roof Coating</li>
    </ul>

    <div class="phone">
      <svg class="phone-icon" viewBox="0 0 28 34"><path d="M8 2c-3 1-5 3-5 7 0 8 6 19 13 22 3 1 5 0 7-2l-4-6-3 2c-3-2-6-8-6-12l3-2-3-8z" fill="var(--white)"/></svg>
      <span>555.214.7736</span>
    </div>

    <div class="website">
      <svg class="globe-icon" viewBox="0 0 40 40" fill="none" stroke="var(--board)" stroke-width="2.2">
        <circle cx="20" cy="20" r="17"/>
        <ellipse cx="20" cy="20" rx="8" ry="17"/>
        <line x1="3" y1="20" x2="37" y2="20"/>
        <line x1="6" y1="11" x2="34" y2="11"/>
        <line x1="6" y1="29" x2="34" y2="29"/>
      </svg>
      <span>www.corvella-roofing-example.com</span>
    </div>
  </section>
</body>
</html>
```